Willow Tri Fold Brochure
Tri Fold Brochure of Salon menu & services
Hello everyone, i have uploaded a few pics for the brochures.
are you prefer any size exactly for brochure ?
Inside sect 1 just design, sect 2 & 3 services, back sct 1 "front" lust design n comp name, back middle comp contact details, back sect 3 about us.
hi, will your brochure be a back to back trifold?..tnx..best regards

```html
<!DOCTYPE html>
<html lang="en">
<head>
<meta charset="utf-8">
<title>Willow Nail Spa Tri Fold Brochure</title>
<link href="https://fonts.googleapis.com/css2?family=Cinzel:wght@600&family=Lato:wght@400;700&family=Great+Vibes&display=swap" rel="stylesheet">
<style>
:root{
  --page:#3b2d24;
  --gold-light:#f4ecd8;
  --gold-mid:#e2d3ae;
  --gold-deep:#c9b384;
  --ink:#4a3a28;
  --accent:#6b2f57;
  --rule:#b59a63;
}
*{box-sizing:border-box;margin:0;padding:0}
html,body{width:1200px;height:490px;overflow:hidden;background:var(--page)}
.canvas{position:relative;width:1200px;height:490px;font-family:"Lato",sans-serif;color:var(--ink)}
.brochure{position:absolute;top:22px;width:555px;height:448px;display:flex;box-shadow:0 4px 14px rgba(0,0,0,.45)}
.brochure.outside{left:30px}
.brochure.inside{left:615px}
.panel{position:relative;width:185px;height:100%;overflow:hidden;
  background:radial-gradient(circle at 50% 40%,var(--gold-light),var(--gold-mid) 60%,var(--gold-deep));
  border-right:1px solid rgba(120,95,50,.25);padding:10px 12px}
.panel:last-child{border-right:none}
.photo{display:block;border-radius:3px}
.heading{font-family:"Cinzel",serif;font-size:10px;letter-spacing:1px;color:var(--accent);
  text-align:center;margin:6px 0 5px;display:flex;align-items:center;gap:5px;justify-content:center}
.heading::before,.heading::after{content:"";flex:1;height:1px;background:var(--rule)}
.body{font-size:6.4px;line-height:1.5;text-align:justify}
.brand{font-family:"Cinzel",serif;font-size:22px;color:var(--accent);display:flex;align-items:center;gap:6px;justify-content:center}
.brand .dot{width:8px;height:8px;border-radius:50%;background:var(--accent)}
.brand-sub{font-family:"Cinzel",serif;font-size:8px;letter-spacing:3px;text-align:center;color:var(--ink);margin-top:2px}
.tagline{font-family:"Great Vibes",cursive;font-size:17px;text-align:center;color:var(--ink);line-height:1.1}
.phone{font-family:"Cinzel",serif;font-size:11px;color:var(--accent);text-align:center;position:absolute;left:0;right:0;bottom:26px}
.contact-block{font-size:6.6px;line-height:1.55;text-align:center;margin-bottom:9px}
.contact-block strong{display:block;font-size:7px;color:var(--accent)}
.menu{font-size:6.4px;line-height:1.55}
.menu li{list-style:none;display:flex;justify-content:space-between}
.menu-title{font-family:"Cinzel",serif;font-size:8px;color:var(--accent);margin:6px 0 2px}
.row{display:flex;gap:6px;align-items:flex-start;margin-top:6px}
.row .photo{flex:none}
</style>
</head>
<body>
<div class="canvas">

  <section class="brochure outside">
    <div class="panel about">
      <svg class="photo" width="161" height="95" role="img" aria-label="Photo of a manicured hand holding a flower">
        <defs><linearGradient id="g1" x1="0" y1="0" x2="1" y2="1"><stop offset="0" stop-color="#f3e4dc"/><stop offset="1" stop-color="#d9b39a"/></linearGradient></defs>
        <rect width="161" height="95" fill="url(#g1)"/></svg>
      <h2 class="heading">About Us</h2>
      <p class="body">Willow Nail Spa is a calm retreat where every visit begins with warm towels, soft music and a careful consultation. Our licensed technicians use gentle products and sterile tools to keep hands and feet healthy and bright. We believe beauty should feel relaxing, so every chair is spaced for privacy and every treatment is unhurried. From a quick polish change to a full spa pedicure, we take pride in clean work, lasting colour and friendly service. Come and unwind with us.</p>
      <p class="body" style="margin-top:5px">Our small team of nail artists loves detail and always has time for a chat.</p>
      <p class="phone">Call Us<br>(555) 014-2298</p>
    </div>

    <div class="panel contact">
      <h2 class="heading" style="margin-top:4px">Contact Us</h2>
      <div class="contact-block"><strong>Willow Nail Spa</strong>210 Garden Row, Suite 4<br>Riverside</div>
      <div class="contact-block"><strong>Opening Hours</strong>Mon – Sat 10am – 8pm<br>Sunday 11am – 6pm</div>
      <div class="contact-block"><strong>Phone</strong>(555) 014-2298</div>
      <div class="contact-block"><strong>Email &amp; Web</strong>hello@willownails.example<br>www.willownails.example</div>
      <svg class="photo" width="161" height="120" style="margin-top:18px" role="img" aria-label="Photo of hands resting in a bowl of water with petals">
        <defs><radialGradient id="g2"><stop offset="0" stop-color="#fbf6ee"/><stop offset="1" stop-color="#e2d3ae"/></radialGradient></defs>
        <rect width="161" height="120" fill="url(#g2)"/></svg>
      <div class="contact-block" style="margin-top:8px"><strong>Gift Certificates</strong>Available in any amount</div>
    </div>

    <div class="panel cover" style="padding:0">
      <svg class="photo" width="185" height="205" role="img" aria-label="Photo of manicured hands with pink roses">
        <defs><linearGradient id="g3" x1="0" y1="0" x2="0" y2="1"><stop offset="0" stop-color="#e9c9d0"/><stop offset="1" stop-color="#e6d7b8"/></linearGradient></defs>
        <rect width="185" height="205" fill="url(#g3)"/></svg>
      <div style="padding:22px 12px 0">
        <div class="brand"><span class="dot"></span>Willow</div>
        <div class="brand-sub">NAIL SPA</div>
        <p class="tagline" style="margin-top:70px">Riverside's most exclusive<br>Nail Spa</p>
      </div>
    </div>
  </section>

  <section class="brochure inside">
    <div class="panel products">
      <p class="body">We carry a wide range of services and quality products to keep your hands and feet looking their best.</p>
      <div class="brand" style="font-size:19px;margin-top:10px"><span class="dot"></span>Willow</div>
      <div class="brand-sub">NAIL SPA</div>
      <h2 class="heading" style="margin-top:10px">Product &amp; Services</h2>
      <svg class="photo" width="161" height="120" style="margin-top:8px" role="img" aria-label="Photo of smiling guests enjoying a spa day">
        <defs><linearGradient id="g4" x1="0" y1="0" x2="1" y2="0"><stop offset="0" stop-color="#8d6aa3"/><stop offset=".5" stop-color="#e6b8c4"/><stop offset="1" stop-color="#d9b39a"/></linearGradient></defs>
        <rect width="161" height="120" fill="url(#g4)"/></svg>
      <svg class="photo" width="110" height="70" style="margin:8px 0 0 25px" role="img" aria-label="Photo of polished fingernails">
        <rect width="110" height="70" fill="#c9a79a"/></svg>
    </div>

    <div class="panel services">
      <div class="menu-title">Manicures</div>
      <ul class="menu">
        <li><span>Classic Manicure</span><span>$15</span></li>
        <li><span>French Manicure</span><span>$20</span></li>
        <li><span>Gel Manicure</span><span>$30</span></li>
        <li><span>Paraffin Manicure</span><span>$25</span></li>
      </ul>
      <div class="menu-title">Pedicures</div>
      <ul class="menu">
        <li><span>Classic Pedicure</span><span>$25</span></li>
        <li><span>Spa Pedicure</span><span>$40</span></li>
        <li><span>Gel Pedicure</span><span>$45</span></li>
        <li><span>Deluxe Pedicure</span><span>$55</span></li>
      </ul>
      <div class="menu-title">Acrylic &amp; Gel</div>
      <ul class="menu">
        <li><span>Full Set</span><span>$35</span></li>
        <li><span>Fill In</span><span>$25</span></li>
        <li><span>Pink &amp; White</span><span>$45</span></li>
      </ul>
      <div class="menu-title">Waxing</div>
      <ul class="menu">
        <li><span>Eyebrow</span><span>$10</span></li>
        <li><span>Lip or Chin</span><span>$8</span></li>
        <li><span>Full Leg</span><span>$50</span></li>
      </ul>
      <div class="menu-title">Add Ons</div>
      <ul class="menu">
        <li><span>Nail Art</span><span>$5</span></li>
        <li><span>Polish Change</span><span>$10</span></li>
        <li><span>Hot Stone Massage</span><span>$15</span></li>
      </ul>
    </div>

    <div class="panel parties">
      <div class="row">
        <h2 class="heading" style="flex:1;margin-top:20px">Private Parties</h2>
        <svg class="photo" width="70" height="50" role="img" aria-label="Photo of painted nails"><rect width="70" height="50" fill="#8d6aa3"/></svg>
      </div>
      <p class="body" style="margin-top:5px">Celebrate with friends in our private lounge. We host bridal showers, birthdays and girls' nights with drinks, music and pampering for every guest.</p>
      <div class="row">
        <svg class="photo" width="40" height="40" role="img" aria-label="Photo of a guest at a spa party"><rect width="40" height="40" fill="#d9b39a"/></svg>
        <p class="body">Parties start at six guests and include a manicure and pedicure for each person.</p>
      </div>
      <div class="row">
        <svg class="photo" width="40" height="40" role="img" aria-label="Photo of a bride's manicured hands"><rect width="40" height="40" fill="#e6b8c4"/></svg>
        <p class="body">Bridal packages add nail art and champagne for the bride and her party.</p>
      </div>
      <div class="row">
        <svg class="photo" width="40" height="40" role="img" aria-label="Photo of a spa gift box"><rect width="40" height="40" fill="#c9b384"/></svg>
        <p class="body">Gift certificates make a lovely present for any occasion.</p>
      </div>
      <p class="body" style="margin-top:6px">Book your party at least one week ahead by phone or email.</p>
    </div>
  </section>

</div>
</body>
</html>
```